Wix web design for healthcare IT consulting firm.

I am looking for a web design built in Wix that it will be easy for me to add or edit content in the future. The web site does not need to be overly complicated, but it should look very polished and professional. I also want to ensure it is mobile device friendly. I do not need any type of on-line purchasing ability. I will eventually do blogs, but for now it is a fairly standard web site with main page, about us, services provided, etc. I would also like a place for potential customers to contact us directly from the web site. I have included a Word document with some content for the web design. I have also included my logo and business card for reference. I would like to utilize similar colors as my business card. One of my primary competitors is https://vonmarlhq.example/

Target Market(s)

Target market could be nursing home CEO, CIO, or other leader at an organization that manages long term care facilities.

Number of Pages Required

5+ page

Colors
876aae

Requirements
Must have
• Be designed to be used in Wix. Use the content I provided to create and make web design. Allow to be viewed on mobile device. Please use similar color structure as attached business card. Please use attached logo in design.

```html
<!DOCTYPE html>
<html lang="en">
<head>
<meta charset="utf-8">
<title>About Us – Brightway Care Solutions</title>
<link rel="stylesheet" href="https://fonts.googleapis.com/css2?family=Open+Sans:wght@300;400;600&family=Arimo:wght@400;700&display=swap">
<style>
  :root {
    --purple: #876aae;
    --purple-deep: #7a5ca3;
    --hero-a: #9d86c4;
    --hero-b: #7d64aa;
    --ink: #222222;
    --mist-blue: #f5f9fd;
    --mist-lilac: #f5f3fd;
    --footer: #222222;
    --footer-base: #1c1c1c;
    --footer-muted: #6e6e6e;
    --white: #ffffff;
  }
  * { box-sizing: border-box; margin: 0; padding: 0; }
  html, body { width: 997px; height: 1200px; overflow: hidden; }
  body { position: relative; font-family: "Open Sans", sans-serif; color: var(--ink); background: var(--white); }

  .site-header {
    position: absolute; top: 0; left: 0; width: 997px; height: 68px;
    background: rgba(255,255,255,0.93); z-index: 2;
  }
  .brand {
    position: absolute; left: 182px; top: 19px; height: 29px;
    display: flex; align-items: center; gap: 5px;
    font-family: "Open Sans", sans-serif; font-weight: 600; font-size: 15px; color: var(--purple);
  }
  .brand-mark { width: 11px; height: 11px; background: var(--purple); }
  .main-nav {
    position: absolute; top: 31px; left: 532px; display: flex; gap: 0;
    font-family: "Arimo", sans-serif; font-size: 8px; color: var(--purple-deep);
  }
  .main-nav a { color: inherit; text-decoration: none; position: absolute; white-space: nowrap; }

  .hero {
    position: absolute; top: 0; left: 0; width: 997px; height: 276px;
    background: linear-gradient(100deg, var(--hero-a) 0%, #9079b8 45%, var(--hero-b) 100%);
  }
  .hero-title {
    position: absolute; top: 212px; width: 100%; text-align: center;
    font-weight: 600; font-size: 23px; color: var(--white); letter-spacing: 0.2px;
  }

  .mission { position: absolute; top: 276px; left: 0; width: 997px; height: 465px; background: var(--mist-blue); }
  .section-heading {
    position: absolute; width: 100%; text-align: center;
    font-weight: 300; font-size: 19.5px; color: var(--ink);
  }
  .mission .section-heading { top: 56px; }
  .mission-text { position: absolute; top: 106px; width: 100%; text-align: center; font-size: 12.3px; }
  .mission-photo {
    position: absolute; left: 299px; top: 144px; width: 400px; height: 266px;
    background: linear-gradient(110deg, #c9c5bb 0%, #e9ece3 45%, #d8dacf 60%, #6d7c8f 100%);
  }

  .niche { position: absolute; top: 741px; left: 0; width: 997px; height: 337px; background: var(--mist-lilac); }
  .niche .section-heading { top: 26px; }
  .niche-card { position: absolute; top: 84px; width: 204px; }
  .niche-photo { width: 204px; height: 147px; }
  .niche-caption { margin-top: 20px; text-align: center; font-size: 12.3px; line-height: 18px; }

  .site-footer { position: absolute; top: 1078px; left: 0; width: 997px; height: 92px; background: var(--footer); }
  .footer-nav { font-family: "Arimo", sans-serif; font-size: 8.5px; font-weight: 700; color: var(--white); }
  .footer-nav a { position: absolute; top: 27px; color: inherit; text-decoration: none; white-space: nowrap; }
  .social { position: absolute; top: 55px; left: 414px; display: flex; gap: 21px; }
  .social span { width: 17px; height: 17px; border-radius: 2px; background: var(--purple); display: block; }
  .footer-base {
    position: absolute; top: 1170px; left: 0; width: 997px; height: 30px;
    background: var(--footer-base); border-top: 1px solid #2b2b2b;
    text-align: center; font-size: 7px; line-height: 28px; color: var(--footer-muted);
  }
</style>
</head>
<body>
  <section class="hero" role="img" aria-label="Purple-tinted desk scene with a hand holding a pen over a printed schedule beside a laptop">
    <h1 class="hero-title">ABOUT US</h1>
  </section>

  <header class="site-header">
    <div class="brand"><span class="brand-mark"></span>Brightway</div>
    <nav class="main-nav">
      <a href="#" style="left:0">Home</a>
      <a href="#" style="left:51px">About Us</a>
      <a href="#" style="left:113px">Services Provided</a>
      <a href="#" style="left:204px">Blog</a>
      <a href="#" style="left:244px">Contact Us</a>
    </nav>
  </header>

  <section class="mission">
    <h2 class="section-heading">Brightway Mission Statement</h2>
    <p class="mission-text">Partner with customers to increase the value of their technology tools</p>
    <div class="mission-photo" role="img" aria-label="Two business partners shaking hands outdoors"></div>
  </section>

  <section class="niche">
    <h2 class="section-heading">Brightway Niche</h2>
    <div class="niche-card" style="left:182px">
      <div class="niche-photo" role="img" aria-label="Consultant and client reviewing a contract at a wooden desk" style="background:linear-gradient(135deg,#6b5a48,#a88f70 50%,#3e4350)"></div>
      <p class="niche-caption">Understand and get to know<br>customer and their needs</p>
    </div>
    <div class="niche-card" style="left:397px">
      <div class="niche-photo" role="img" aria-label="Handshake between two people in business suits" style="background:linear-gradient(135deg,#2e2b2c,#6a6464 50%,#d9d6d2)"></div>
      <p class="niche-caption">Committed to be a<br>partner, not vendor</p>
    </div>
    <div class="niche-card" style="left:612px">
      <div class="niche-photo" role="img" aria-label="Team gathered around a laptop in an office meeting" style="background:linear-gradient(135deg,#4a4a52,#8c8a88 50%,#5a4a40)"></div>
      <p class="niche-caption">Provide simplified change<br>management expertise</p>
    </div>
  </section>

  <footer class="site-footer">
    <nav class="footer-nav">
      <a href="#" style="left:339px">Home</a>
      <a href="#" style="left:397px">About Us</a>
      <a href="#" style="left:468px">Services Provided</a>
      <a href="#" style="left:572px">Blog</a>
      <a href="#" style="left:619px">Contact Us</a>
    </nav>
    <div class="social" aria-label="Social links">
      <span></span><span></span><span></span><span></span><span></span>
    </div>
  </footer>
  <div class="footer-base">BRIGHTWAY CARE &nbsp;&nbsp; 2019 / All Rights Reserved</div>
</body>
</html>
```